Produktetikett für Mikronährstoffe
Wir sind sehr zufrieden und schätzen die schnelle Umsetzung von Änderungswünschen. Herzlichen Dank an Bertram
Zielgruppe
Herstellung und Vertrieb von Desinfektionsmitteln und jetz neu Mikronährstoffe. Und darum geht es. Wir möchten ein Etikett gestalten lassen das modern ist und trotzdem unsere Firmenfarben und unser Logo (evtl. stilisiert) enthält. Wahrscheinlich werden wir eine braune Flasche (ähnl. Apothekerflaschen) wählen.
Aufgabenstellung
Produktetikett für Mikronährstoffe (im Nahrungsergänzungsbereich) Die Ausführung der Flasche ist noch nicht bekannnt, jedoch schwebt uns eine braune oder dunkelgrüne Flasche vor. Auch gibt es noch keinen Namen für das Produkt.

```html
<!DOCTYPE html>
<html lang="de">
<head>
<meta charset="utf-8">
<title>VELOMAR Mikronährstoffe – Etikett</title>
<link rel="stylesheet" href="https://fonts.googleapis.com/css2?family=Montserrat:wght@500;700;800&display=swap">
<style>
  :root {
    --backdrop: #a7a7a7;
    --label-white: #ffffff;
    --brand-blue: #0aa3c7;
    --brand-green: #7db443;
    --lime: #d6dc2e;
    --leaf-green: #78ae3f;
    --text-white: #ffffff;
  }
  html, body {
    margin: 0;
    padding: 0;
    width: 764px;
    height: 1200px;
    overflow: hidden;
    background: var(--backdrop);
  }
  .canvas {
    position: relative;
    width: 764px;
    height: 1200px;
  }
  .product-label {
    position: absolute;
    left: 32px;
    top: 328px;
    width: 700px;
    height: 543px;
    background: var(--label-white);
    box-shadow: 0 6px 14px rgba(0,0,0,0.25);
  }
  .product-label svg {
    display: block;
    width: 100%;
    height: 100%;
  }
  .brand-name {
    font-family: "Montserrat", sans-serif;
    font-weight: 500;
    fill: var(--brand-blue);
  }
  .product-title {
    font-family: "Montserrat", sans-serif;
    font-weight: 800;
    fill: var(--brand-blue);
  }
  .product-category {
    font-family: "Montserrat", sans-serif;
    font-weight: 800;
    fill: var(--brand-green);
  }
  .ingredient-list,
  .net-weight {
    font-family: "Montserrat", sans-serif;
    font-weight: 700;
    fill: var(--text-white);
  }
  .count-number {
    font-family: "Montserrat", sans-serif;
    font-weight: 800;
    fill: var(--brand-blue);
  }
  .count-unit {
    font-family: "Montserrat", sans-serif;
    font-weight: 800;
    fill: var(--brand-green);
  }
</style>
</head>
<body>
<main class="canvas">
  <section class="product-label">
    <svg viewBox="0 0 1156 896" xmlns="http://www.w3.org/2000/svg">
      <defs>
        <radialGradient id="green-wave-fill" cx="560" cy="560" r="600" gradientUnits="userSpaceOnUse">
          <stop offset="0" stop-color="#dcdc2e"/>
          <stop offset="0.55" stop-color="#9fc23c"/>
          <stop offset="1" stop-color="#78ae3f"/>
        </radialGradient>
        <linearGradient id="produce-fill" x1="0" y1="0" x2="1" y2="1">
          <stop offset="0" stop-color="#f07a1f"/>
          <stop offset="0.5" stop-color="#f6c21d"/>
          <stop offset="1" stop-color="#6a5a8a"/>
        </linearGradient>
        <path id="category-arc" d="M 262 560 Q 640 390 1030 512"/>
      </defs>

      <text class="brand-name" x="555" y="135" font-size="70" text-anchor="middle" letter-spacing="2">VELOMAR</text>

      <text class="product-title" x="578" y="390" font-size="118" text-anchor="middle" textLength="945" lengthAdjust="spacingAndGlyphs">Mikronährstoffe</text>

      <path class="green-wave" fill="url(#green-wave-fill)"
            d="M 240 640 C 360 540 520 490 680 495 C 840 500 960 560 1156 520 L 1156 896 L 0 896 L 0 850 Z"/>

      <path class="blue-band" fill="var(--brand-blue)"
            d="M 95 860 C 400 842 700 800 862 716 C 700 772 420 792 225 770 C 180 800 130 835 95 860 Z"/>

      <path class="blue-corner" fill="var(--brand-blue)"
            d="M 1156 520 L 1156 896 L 875 896 C 960 800 1060 680 1156 520 Z"/>

      <path class="produce-photo" role="img" aria-label="Foto: Paprika, Trauben und Limette"
            fill="url(#produce-fill)"
            d="M 0 530 C 100 505 220 540 300 600 L 262 700 L 200 790 L 95 860 L 0 860 Z"/>

      <text class="product-category" font-size="50">
        <textPath href="#category-arc">Nahrungsergänzungsmittel</textPath>
      </text>

      <text class="ingredient-list" font-size="28" text-anchor="middle">
        <tspan x="560" y="620">Vitamine, Mineralstoffe,</tspan>
        <tspan x="560" y="660">Spurenelemente, Pflanzenstoffe</tspan>
        <tspan x="560" y="700">und Omega-3-Fettsäuren.</tspan>
      </text>

      <g class="capsule-count">
        <circle cx="1040" cy="720" r="100" fill="#c4dc6a"/>
        <circle cx="1040" cy="720" r="90" fill="var(--label-white)"/>
        <text class="count-number" x="1040" y="730" font-size="92" text-anchor="middle">60</text>
        <text class="count-unit" x="1040" y="768" font-size="24" text-anchor="middle">Capsules</text>
      </g>

      <text class="net-weight" x="695" y="838" font-size="24">Net Weight 65 g</text>
    </svg>
  </section>
</main>
</body>
</html>
```